Cafe Opening Flyer Design Project

We need a flyer for the grand opening of our new cafe. It should appeal very much to our target consumer - working adults within the CBD area, where there is substantial competition as well.

Keep the message clear to the audience:
(below statements are just examples, please be creative and come up with your own phrases)
1. there's a new cafe you don't wanna miss out..
2. and coffee is always a good idea..

Be bold and creative!
Updates

Dear designers,

Kindly add in our opening hours on the flyer (A5 size, single side)
Weekdays: 7am to 6pm
Sat: 8am to 3pm
Closed on Sun & PH

Thank you!

Target Market(s)

Working adults in the CBD area, coffee lovers

Industry/Entity Type

Cafe

Requirements
Must have
• Location:
24 Brindlemere Wharf, The Linden Court #03-18

```html
<!DOCTYPE html>
<html lang="en">
<head>
<meta charset="utf-8">
<title>Warmly Brewed – Grand Opening Flyer</title>
<link href="https://fonts.googleapis.com/css2?family=Cinzel:wght@700&family=EB+Garamond:wght@500;600;700&display=swap" rel="stylesheet">
<style>
  :root {
    --stage: #2e2e2e;
    --burlap-light: #c2a57c;
    --burlap-mid: #b09068;
    --burlap-dark: #8c7050;
    --band: #3a2b21;
    --gold: #c9a465;
    --gold-light: #e0c597;
    --cream: #efe3c8;
    --frame: #f4f1ea;
    --coffee: #2a1a10;
  }
  * { margin: 0; padding: 0; box-sizing: border-box; }
  html, body { width: 1200px; height: 1000px; overflow: hidden; background: var(--stage); }
  .canvas { position: relative; width: 1200px; height: 1000px; }

  .flyer {
    position: absolute; left: 333px; top: 120px; width: 557px; height: 792px; overflow: hidden;
    background:
      repeating-linear-gradient(0deg, rgba(60,40,20,0.06) 0 1px, rgba(0,0,0,0) 1px 3px),
      repeating-linear-gradient(90deg, rgba(60,40,20,0.06) 0 1px, rgba(0,0,0,0) 1px 3px),
      linear-gradient(180deg, var(--burlap-light) 0%, var(--burlap-mid) 55%, var(--burlap-dark) 100%);
  }
  .ornament {
    position: absolute; left: 0; top: 140px; width: 557px; height: 520px;
    background:
      radial-gradient(ellipse at 50% 50%, rgba(90,45,30,0.42) 0%, rgba(90,45,30,0.18) 42%, rgba(90,45,30,0) 68%),
      radial-gradient(ellipse at 50% 92%, rgba(90,45,30,0.28) 0%, rgba(90,45,30,0) 45%);
  }

  .top-band {
    position: absolute; left: 0; top: 63px; width: 100%; height: 82px; background: var(--band);
  }
  .top-band .word {
    position: absolute; top: 26px;
    font-family: "Cinzel", serif; font-weight: 700; font-size: 25px; letter-spacing: 0.5px; color: var(--gold);
  }
  .word.left { left: 25px; }
  .word.right { left: 408px; }

  .brand {
    position: absolute; left: 191px; top: 16px; width: 176px; height: 176px; border-radius: 50%;
    background: var(--band);
    display: flex; align-items: center; justify-content: center; text-align: center;
    font-family: "EB Garamond", serif; font-weight: 600; font-size: 30px; line-height: 1.05; color: var(--gold);
  }

  .polaroid {
    position: absolute; background: var(--frame); padding: 11px 11px 52px;
    box-shadow: 0 4px 10px rgba(0,0,0,0.35);
  }
  .polaroid .photo { width: 100%; height: 100%; }
  .polaroid.left { left: 24px; top: 170px; width: 213px; height: 245px; transform: rotate(-4deg); }
  .polaroid.left .photo {
    background:
      radial-gradient(ellipse at 62% 82%, #8a5a34 0%, rgba(138,90,52,0) 38%),
      radial-gradient(ellipse at 22% 70%, #e6ddd0 0%, rgba(230,221,208,0) 22%),
      radial-gradient(circle at 60% 25%, #7a3822 0%, #4a2416 50%, #2a140c 100%);
  }
  .polaroid.right { left: 332px; top: 175px; width: 205px; height: 245px; transform: rotate(5deg); }
  .polaroid.right .photo {
    background:
      radial-gradient(ellipse 44% 26% at 50% 38%, #e3c29a 0%, #c8955e 60%, rgba(80,60,50,0) 100%),
      linear-gradient(180deg, #3a3632 0%, #5c534b 55%, #2a2622 100%);
  }

  .cup {
    position: absolute; left: 167px; top: 258px; width: 224px; height: 224px; border-radius: 50%;
    background: radial-gradient(circle, #4a3222 0%, var(--coffee) 52%, #a07850 60%, #ffffff 64%, #e9e6e1 100%);
    box-shadow: 0 6px 14px rgba(0,0,0,0.4);
  }

  .headline {
    position: absolute; left: 0; top: 346px; width: 100%; padding-left: 20px; text-align: center;
    font-family: "Cinzel", serif; font-weight: 700; font-size: 32px; color: var(--gold-light);
    text-shadow: -1px -1px 0 #5a3a22, 1px -1px 0 #5a3a22, -1px 1px 0 #5a3a22, 1px 1px 0 #5a3a22, 0 3px 6px rgba(0,0,0,0.5);
  }

  .tagline-band {
    position: absolute; left: 0; top: 492px; width: 100%; height: 56px; background: var(--band);
    font-family: "EB Garamond", serif; font-weight: 600; font-size: 18px; letter-spacing: 0.3px; color: var(--gold);
    line-height: 1;
  }
  .tagline-band .line { position: absolute; white-space: nowrap; }
  .line.first { left: 10px; top: 8px; }
  .line.second { right: 22px; top: 32px; }

  .hours {
    position: absolute; left: 14px; top: 588px; width: 190px;
    font-family: "EB Garamond", serif; font-weight: 700; font-size: 14px; line-height: 1.3; color: var(--band);
  }
  .hours .label { font-family: "Cinzel", serif; font-size: 13px; letter-spacing: 0.5px; }

  .address {
    position: absolute; right: 0; top: 594px; height: 44px; padding: 0 22px; background: var(--band);
    display: flex; align-items: center; white-space: nowrap;
    font-family: "EB Garamond", serif; font-weight: 500; font-size: 16px; color: var(--cream);
  }

  .beans {
    position: absolute; left: 0; top: 680px; width: 100%; height: 112px;
    background:
      radial-gradient(ellipse 60% 50% at 50% 30%, #6a3420 0%, rgba(106,52,32,0) 100%),
      linear-gradient(180deg, #3b1d12 0%, #5a2c18 45%, #7a4a28 70%, #9a6a3e 100%);
  }
</style>
</head>
<body>
<div class="canvas">
  <div class="flyer">
    <div class="ornament" role="img" aria-label="Brown damask scroll ornament behind the coffee cup"></div>

    <div class="top-band">
      <span class="word left">PREMIUM</span>
      <span class="word right">QUALITY</span>
    </div>
    <div class="brand">Warmly<br>Brewed</div>

    <div class="polaroid left"><div class="photo" role="img" aria-label="Photo of a cup of coffee with cinnamon sticks and roasted beans"></div></div>
    <div class="polaroid right"><div class="photo" role="img" aria-label="Photo of a latte with leaf latte art"></div></div>

    <div class="cup" role="img" aria-label="Top view of a steaming cup of black coffee"></div>

    <div class="headline">GRAND OPENING!</div>

    <div class="tagline-band">
      <span class="line first">THERE'S A NEW CAFE YOU DON'T WANNA MISS OUT..</span>
      <span class="line second">COFFEE IS ALWAYS A GOOD IDEA..</span>
    </div>

    <div class="hours">
      <div class="label">OPENING HOURS</div>
      <div>Weekdays: 7am to 6pm</div>
      <div>Sat: 8am to 3pm</div>
      <div>Closed on Sun &amp; PH</div>
    </div>

    <div class="address">24 Brindlemere Wharf, The Linden Court #03-18</div>

    <div class="beans" role="img" aria-label="Roasted coffee beans scattered on a wooden table"></div>
  </div>
</div>
</body>
</html>
```